Information Package (Hail Insurance Claim)

TheBrightwaveGroup.com is a new company to the Calgary Alberta area. We want a flyer for potential clients to give them tips on how to deal with the insurance process, how we can represent them, and what to do for next steps.
Also in the flyer we want to introduce clients to the products we use along with the experience we have.

Target Market(s)

Homeowners who have just got hit with hail

Font styles to use
Serif

Requirements
Must have
• Must have two sides.
phone number is 403-555-0187
email is Claims@TheBrightwaveGroup.com
Trusted Brands: Tolvinder, Bratley Fenwicking, ZUP, RMT
Bratley fenwick website has their roofing products and system we use.
I have attached our logo design and want to keep that theme.
Also this link https://northfieldtopsquad.com/roof-insurance-claims/ has some great information on steps.
Products to include from these links: https://www.bratleyfenwick.com/roofing/shingles
https://www.marlowtopsinc.ca/roof-shingles-types/

```html
<!DOCTYPE html>
<html lang="en">
<head>
<meta charset="utf-8">
<title>The Brightwave Group – Hail Insurance Claim Flyer</title>
<link href="https://fonts.googleapis.com/css2?family=Signika:wght@500;600;700&family=Source+Sans+3:wght@400;600;700&display=swap" rel="stylesheet">
<style>
:root{
  --teal:#5ec3be;
  --teal-dark:#3fa9a4;
  --navy:#2b3a55;
  --navy-soft:#3d4d6b;
  --yellow:#f5c04d;
  --red:#e0262d;
  --white:#ffffff;
  --ink:#1f2a3d;
  --stage:#8a8a8a;
}
*{box-sizing:border-box;margin:0;padding:0}
html,body{width:1200px;height:846px;overflow:hidden;background:var(--stage)}
body{position:relative;font-family:"Source Sans 3",sans-serif;color:var(--ink)}
.page{position:absolute;top:64px;width:554px;height:716px;overflow:hidden;background:var(--teal)}
.page--front{left:40px}
.page--back{left:614px;width:550px;background:var(--white)}
.bg{position:absolute;inset:0;width:100%;height:100%}
.abs{position:absolute}
.heading{font-family:"Signika",sans-serif;font-weight:700}

/* front */
.brand-name{left:22px;top:52px;width:240px;font-family:"Signika",sans-serif;font-weight:700;font-size:24px;color:var(--navy);display:flex;align-items:center;gap:8px}
.brand-name .dot{width:16px;height:16px;background:var(--teal);flex:none}
.roof-art{left:322px;top:16px;width:230px;height:186px;background:linear-gradient(135deg,#3a3a3a 0%,#2c2c2c 45%,#c98e4e 60%,#e6b27a 100%);clip-path:polygon(0 60%,55% 0,100% 45%,100% 100%,20% 100%)}
.layer{right:248px;font-family:"Signika",sans-serif;font-size:10px;color:#6a6a6a;display:flex;align-items:center;gap:6px;letter-spacing:.5px}
.layer span{display:block;width:20px;height:20px;background:var(--red)}
.title-main{left:70px;top:150px;font-size:42px;color:var(--red);letter-spacing:-1px}
.subtitle{left:12px;top:196px;font-size:20px;color:var(--red);letter-spacing:-.5px}
.tags{left:0;top:226px;width:554px;height:19px;background:var(--white);display:flex;font-size:11px;font-weight:600;color:var(--navy)}
.tags li{list-style:none;padding:1px 5px 0 8px;border-right:2px solid var(--teal)}
.tags li:first-child{background:var(--yellow)}
.steps{left:12px;top:262px;width:530px;height:222px;background:var(--navy-soft);border-radius:18px;color:var(--white);font-size:10.5px;line-height:1.25}
.pill{background:var(--white);color:var(--red);border-radius:14px;font-family:"Signika",sans-serif;font-weight:700;text-align:center;padding:2px 14px}
.steps-title{left:128px;top:256px;font-size:19px}
.col{position:absolute;top:36px}
.col--l{left:10px;width:300px}
.col--r{left:322px;width:200px;border-left:1px dashed #8090aa;padding-left:10px;height:180px;top:28px;padding-top:8px}
.tick{display:flex;gap:6px;margin-bottom:10px}
.tick svg{flex:none;margin-top:1px}
.hl{color:var(--yellow)}
.num{display:inline-flex;width:11px;height:11px;border-radius:50%;background:var(--yellow);color:var(--navy);font-size:8px;font-weight:700;align-items:center;justify-content:center;margin-right:3px}
.sign{padding-left:16px;text-indent:-14px;margin-left:6px}
.chim-title{left:85px;top:508px;font-size:19px}
.chim-text{left:40px;top:544px;width:474px;text-align:center;color:var(--white);font-size:11.5px;line-height:1.35}
.house-art{left:0;top:592px;width:344px;height:124px;background:linear-gradient(160deg,#a9aaa8,#6e706f);clip-path:polygon(0 70%,55% 0,100% 90%,100% 100%,0 100%)}
.contact{right:10px;font-family:"Signika",sans-serif;font-weight:700;color:var(--white);display:flex;align-items:center;gap:6px;font-size:15px}
.contact.city{color:var(--yellow)}
.contact i{display:flex;width:18px;height:18px;border-radius:50%;background:var(--yellow);align-items:center;justify-content:center}

/* back */
.sec-title{left:0;width:550px;top:14px;display:flex;align-items:center;gap:6px;padding:0 38px;font-size:17px;color:var(--navy)}
.sec-title::before,.sec-title::after{content:"";flex:1;height:1px;background:var(--navy)}
.swatches{left:37px;display:grid;grid-template-columns:repeat(7,64px);column-gap:5px}
.swatch div{height:64px}
.swatch p{font-size:8.5px;text-align:center;margin-top:7px;color:var(--ink)}
.brands{left:0;top:210px;width:550px;height:36px;display:flex;align-items:center;justify-content:center;gap:10px;font-size:17px;color:var(--navy);font-family:"Signika",sans-serif;font-weight:600}
.pref-title{left:112px;top:254px;background:var(--navy);color:var(--yellow);font-size:15.5px;border-radius:14px;padding:3px 16px}
.pref-line{left:62px;top:266px;width:426px;height:1px;background:var(--navy)}
.avatar{left:18px;top:300px;width:132px;height:132px;border-radius:50%;border:6px solid var(--red);background:radial-gradient(circle,#f1d6b4 0 40%,#5ec3be 41% 100%)}
.pref-text{left:158px;top:283px;width:380px;font-size:11.5px;line-height:1.32}
.pref-text b{font-weight:700}
.red{color:var(--red)}
.decide{left:158px;top:394px;width:372px;background:var(--white);padding:2px 6px 3px;font-size:12px;line-height:1.25}
.mis-head{left:13px;top:447px;width:526px;height:21px;border-radius:11px;background:linear-gradient(90deg,var(--navy) 0 58%,var(--red) 58%);color:var(--white);font-family:"Signika",sans-serif;font-weight:700;font-size:14px;padding:1px 0 0 28px;letter-spacing:.3px}
.mis-box{left:13px;top:468px;width:526px;height:112px;background:var(--white);border-radius:0 0 12px 12px;border:1px solid var(--navy);border-top:none;display:flex;gap:8px;padding:4px 8px;font-size:9px;line-height:1.4}
.mis-box ol{list-style:none;flex:1}
.mis-box li{padding-left:12px;position:relative}
.mis-box li::before{content:attr(data-n);position:absolute;left:0;top:2px;width:8px;height:8px;border-radius:50%;background:currentColor;color:inherit}
.mis-box li:nth-child(even){color:var(--red)}
.mis-box .n{position:absolute;left:0;top:2px;width:8px;height:8px;border-radius:50%;background:currentColor}
.mis-box li::before{display:none}
.cta{left:13px;top:590px;font-size:21px;color:var(--red)}
.cta span{color:var(--navy)}
.phone{left:13px;top:612px;font-size:33px;color:var(--navy);display:flex;align-items:center;gap:6px}
.seal{left:264px;top:620px;width:84px;height:84px;border-radius:50%;background:var(--red);border:4px solid var(--white);box-shadow:0 0 0 2px var(--red)}
.badge{left:12px;top:658px;width:30px;height:46px;background:var(--white);border:1px solid var(--navy);border-radius:3px}
.brand-back{left:370px;top:634px;font-family:"Signika",sans-serif;font-weight:700;font-size:19px;color:var(--navy);display:flex;align-items:center;gap:6px}
.brand-back .dot{width:14px;height:14px;background:var(--teal)}
</style>
</head>
<body>

<!-- FRONT -->
<section class="page page--front">
  <svg class="bg" viewBox="0 0 554 716" preserveAspectRatio="none" aria-hidden="true">
    <rect width="554" height="716" fill="var(--teal)"/>
    <polygon points="0,0 470,0 0,240" fill="var(--white)"/>
    <polygon points="554,280 554,560 380,640" fill="var(--yellow)"/>
    <polygon points="0,300 40,300 0,330" fill="var(--yellow)"/>
    <polygon points="554,560 554,716 300,716" fill="var(--navy)"/>
  </svg>

  <div class="abs brand-name"><span class="dot"></span>The Brightwave Group</div>

  <div class="abs roof-art" role="img" aria-label="Cutaway illustration of a roof showing shingles, underlayment and wooden trusses"></div>
  <div class="abs layer" style="top:35px">BREATHE <span></span></div>
  <div class="abs layer" style="top:84px;right:280px">DEFEND <span></span></div>
  <div class="abs layer" style="top:133px;right:310px">SEAL <span></span></div>

  <h1 class="abs heading title-main">Happy Homes</h1>
  <p class="abs heading subtitle">Protected By Experts, Build By Trust.</p>

  <ul class="abs tags">
    <li>Hail Resoration</li><li>Fire &amp; Flood Restoration</li><li>Insurance Claims Liaison Service</li><li>Covid 19 Prevention &amp; Sanitation</li>
  </ul>

  <div class="abs steps">
    <div class="col col--l">
      <div class="tick"><svg width="11" height="11" viewBox="0 0 12 12"><path d="M6 0l6 2v4c0 3-3 5-6 6C3 11 0 9 0 6V2z" fill="#fff"/><path d="M3 6l2 2 4-4" stroke="var(--navy)" stroke-width="1.6" fill="none"/></svg>
        <p>Severe wind and hail can cause major damage to your shingles. <span class="hl">Spot it.</span> Hail damage removes some of the granules from your shingles and speeds up the aging of your shingles.</p></div>
      <div class="tick" style="margin-bottom:0"><svg width="11" height="11" viewBox="0 0 12 12"><path d="M6 0l6 2v4c0 3-3 5-6 6C3 11 0 9 0 6V2z" fill="#fff"/><path d="M3 6l2 2 4-4" stroke="var(--navy)" stroke-width="1.6" fill="none"/></svg>
        <p class="hl">Look for these three signs</p></div>
      <p class="sign"><span class="num">1</span>An asphalt shingle hit by hail will show a bruise - a dark spot where the granules have been knocked off, exposing the asphalt. If it's a brand new hit, the spot will be shiny by freshly exposed asphalt.</p>
      <p class="sign"><span class="num">2</span>Hail may also dent the metal components - flashing, valleys &amp; gutters.</p>
      <p class="sign"><span class="num">3</span>Even if you don't want to get up in your roof, you can simply check your gutters and downspouts for an unusual amount of granules - displaced from the shingles.</p>
    </div>
    <div class="col col--r">
      <div class="tick"><svg width="11" height="11" viewBox="0 0 12 12"><path d="M6 0l6 2v4c0 3-3 5-6 6C3 11 0 9 0 6V2z" fill="#fff"/><path d="M3 6l2 2 4-4" stroke="var(--navy)" stroke-width="1.6" fill="none"/></svg>
        <p>You will probably need to replace the entire roof. Call Us and we'll thoroughly inspect and provide a complete report for your insurance company. We record the exact date the damage occurred and notify the insurance company.</p></div>
      <div class="tick"><svg width="11" height="11" viewBox="0 0 12 12"><path d="M6 0l6 2v4c0 3-3 5-6 6C3 11 0 9 0 6V2z" fill="#fff"/><path d="M3 6l2 2 4-4" stroke="var(--navy)" stroke-width="1.6" fill="none"/></svg>
        <p>Insurance companies like to minimize their claims. You have the right to choose your own contractor and should take as much care in doing so as you would if the insurance company was not involved.</p></div>
    </div>
  </div>
  <h2 class="abs pill steps-title">Easy Steps for Roof Insurance claim</h2>

  <h2 class="abs pill chim-title">Chimney Flashing: A Major Cause of Roof Leaks</h2>
  <p class="abs chim-text">Chimney flashing must be properly installed to prevent expensive leaks. When it is installed the right way, it creates a countering system, where everything overlaps in the right direction to create positive water flow that uses gravity to draw water down and away.</p>

  <div class="abs house-art" role="img" aria-label="Shingled rooftop with chimneys and skylights under a sky with clouds"></div>

  <p class="abs contact city" style="top:637px"><i><svg width="11" height="11" viewBox="0 0 12 12"><path d="M6 1L1 6h2v5h6V6h2z" fill="var(--navy)"/></svg></i>Calgary Alberta</p>
  <p class="abs contact" style="top:664px"><i><svg width="11" height="11" viewBox="0 0 12 12"><circle cx="6" cy="6" r="5" fill="none" stroke="var(--navy)" stroke-width="1.3"/><path d="M1 6h10M6 1v10" stroke="var(--navy)" stroke-width="1"/></svg></i>TheBrightwaveGroup.com</p>
  <p class="abs contact" style="top:688px"><i style="color:var(--navy);font-size:12px">@</i>Claims@TheBrightwaveGroup.com</p>
</section>

<!-- BACK -->
<section class="page page--back">
  <svg class="bg" viewBox="0 0 550 716" preserveAspectRatio="none" aria-hidden="true">
    <rect width="550" height="716" fill="var(--white)"/>
    <polygon points="470,0 550,0 550,40" fill="var(--teal)"/>
    <polygon points="0,206 550,190 550,530 0,560" fill="var(--yellow)"/>
    <polygon points="0,580 550,520 550,716 0,716" fill="var(--yellow)"/>
    <polygon points="0,640 80,716 0,716" fill="var(--navy)"/>
    <rect x="70" y="686" width="30" height="30" fill="var(--yellow)" stroke="#fff"/>
    <rect x="96" y="666" width="30" height="30" fill="var(--teal)"/>
    <rect x="118" y="686" width="18" height="16" fill="var(--navy)"/>
    <rect x="132" y="674" width="12" height="12" fill="var(--red)"/>
  </svg>

  <h2 class="abs heading sec-title">Types of Roof Shingles</h2>

  <div class="abs swatches" style="top:38px">
    <div class="swatch"><div role="img" aria-label="Amber shingle sample" style="background:#a69478"></div><p>Amber</p></div>
    <div class="swatch"><div role="img" aria-label="Onyx black shingle sample" style="background:#1e2020"></div><p>OnyxBlack</p></div>
    <div class="swatch"><div role="img" aria-label="Colonial shingle sample" style="background:#5d5d5b"></div><p>Colonial</p></div>
    <div class="swatch"><div role="img" aria-label="Chateau green shingle sample" style="background:#27564a"></div><p>ChateauGreen</p></div>
    <div class="swatch"><div role="img" aria-label="Driftwood shingle sample" style="background:#6c625b"></div><p>Driftwood</p></div>
    <div class="swatch"><div role="img" aria-label="Antique silver shingle sample" style="background:#8f9697"></div><p>AntiqueSilver</p></div>
    <div class="swatch"><div role="img" aria-label="Pacific wave shingle sample" style="background:#3e464b"></div><p>PacificWave</p></div>
  </div>
  <div class="abs swatches" style="top:122px">
    <div class="swatch"><div role="img" aria-label="Riviera red shingle sample" style="background:#6e2b27"></div><p>Riviera Red</p></div>
    <div class="swatch"><div role="img" aria-label="Weatherwood shingle sample" style="background:#84735a"></div><p>WhetherWood</p></div>
    <div class="swatch"><div role="img" aria-label="Earthtone cedar shingle sample" style="background:#b48455"></div><p>Earthtone Cedar</p></div>
    <div class="swatch"><div role="img" aria-label="National blue shingle sample" style="background:#33323f"></div><p>National Blue</p></div>
    <div class="swatch"><div role="img" aria-label="Super white shingle sample" style="background:#d6d9d8"></div><p>Super White</p></div>
    <div class="swatch"><div role="img" aria-label="Aged redwood shingle sample" style="background:#6a4037"></div><p>Aged Redwood</p></div>
    <div class="swatch"><div role="img" aria-label="Charcoal grey shingle sample" style="background:#505253"></div><p>Charcoal Grey</p></div>
  </div>

  <p class="abs brands">
    <svg width="24" height="24" viewBox="0 0 24 24"><path d="M12 1l3.2 7 7.6.7-5.7 5 1.7 7.5L12 17.3 5.2 21.2l1.7-7.5-5.7-5L8.8 8z" fill="var(--navy)"/></svg>
    Trusted Brands: Tolvinder, Bratley Fenwicking, ZUP, RMT
    <svg width="24" height="24" viewBox="0 0 24 24"><path d="M12 1l3.2 7 7.6.7-5.7 5 1.7 7.5L12 17.3 5.2 21.2l1.7-7.5-5.7-5L8.8 8z" fill="var(--navy)"/></svg>
  </p>

  <div class="abs pref-line"></div>
  <h2 class="abs heading pref-title">Preferred Contractors for Insurance Claim</h2>

  <div class="abs avatar" role="img" aria-label="Cartoon mascot of a roofing expert inside a red ring"></div>
  <div class="abs pref-text">
    <p>Preferred Contractors are in a difficult situation.</p>
    <p><b>A substantial source of their revenue comes from insurance company referrals and naturally, they don't want to jeopardize this valuable source of business.</b></p>
    <p>On the other hand you are their real client and they don't want to damage their reputation by doing a mediocre.</p>
    <p class="red">The bottom line?</p>
  </div>
  <p class="abs decide">It's up to you to decide whose needs are most important to the recommended contractor.</p>

  <h2 class="abs mis-head">10 MISCONCEPTIONS ABOUT INSURANCE CLAIM AND HAIL DAMAGE</h2>
  <div class="abs mis-box">
    <ol>
      <li><span class="n"></span>You're waiting to file your claim.</li>
      <li><span class="n"></span>You think you have to use your insurer's preferred contractors.</li>
      <li><span class="n"></span>You're not sure if you have hail damage.</li>
      <li><span class="n"></span>You don't think you have enough damage to file a claim.</li>
      <li><span class="n"></span>You have a new home and believe the Prairie New Home Warranty Program will cover the hail damage.</li>
      <li><span class="n"></span>You believe the single manufacturer or roofing contractor warranties will cover the hail damage.</li>
    </ol>
    <ol>
      <li><span class="n"></span>You don't want to file a claim because you don't want your policy cancelled or your rates to increase.</li>
      <li><span class="n"></span>You filed a claim but want to wait until the spring or summer to get quotes to have the work done.</li>
      <li><span class="n"></span>You received a payout from your insurance company &amp; you'll find your own contractor, but there's no rush.</li>
      <li><span class="n"></span>You filed a claim but it was denied.</li>
    </ol>
  </div>

  <p class="abs heading cta">For the complete care of home <span>HIRE US!</span></p>
  <p class="abs heading phone">
    <svg width="20" height="20" viewBox="0 0 20 20"><circle cx="10" cy="10" r="9" fill="none" stroke="var(--navy)" stroke-width="2"/><path d="M6.5 5.5l2 0 1 2.5-1.2 1a6 6 0 0 0 2.7 2.7l1-1.2 2.5 1v2c-4 .5-8.5-4-8-8z" fill="var(--navy)"/></svg>
    403-555-0187
  </p>
  <div class="abs seal" role="img" aria-label="Quality guarantee seal"></div>
  <div class="abs badge" role="img" aria-label="Accreditation badge"></div>
  <p class="abs brand-back"><span class="dot"></span>The Brightwave Group</p>
</section>

</body>
</html>
```